Website Design Required

Our client needs a website built from scratch. The website is called Snaps4Wall and is essentially a website that allows you to upload a photo, order and pay and your photo is printed onto a canvas. A closely related website is http://www.framelyte.co.za/ however this project needs a clean, fresh design that encourages purchases.

Snaps4wall will be a dedicated website which allows users to upload and print a single image for large format printing.

The website flow will consist of the following:

• A landing page will be designed which showcases the product offering and offers simple and easy to understand instructions on how to get a photo up- loaded and delivered to their door.

• An upload page will exist that allows users the ability to upload a photo to the website for printing.

• Once the user has uploaded a photo the website will ensure that the dimensions are good enough for printing onto canvas and advise the user accordingly if it is not suitable.
• Once the photo has passed this validation we will take the user to a new page that will give them a preview of their photo. Here they will be given a chance to place the photo correctly should the need arise.

• Once the user is happy with the photo placement they will click on the next button which will take them to the payment and delivery page whereby they will need to complete all the fields.

• Once done, a final order page will appear confirming all the details of the order as well as payment and delivery information. Once the user is satisfied he can click the order button.

Requirements
Must have
• We will need the following pages designed:
1. Homepage
2. Upload page
3. Photo placement page (which allows users to align their photo onto the canvas)
4. Order & Payment page
Should not have
• The design should not use old style fonts and shoddy illustrations. If illustrations are used they have to be clean, simple, stylish.

```html
<!DOCTYPE html>
<html lang="en">
<head>
<meta charset="utf-8">
<title>Snaps4Wall</title>
<link href="https://fonts.googleapis.com/css2?family=Arimo:wght@400;700&family=PT+Sans:wght@400;700&family=PT+Serif:ital@1&display=swap" rel="stylesheet">
<style>
:root{
  --hero-dark:#6e4a43;
  --hero-mid:#9a6d63;
  --hero-light:#c39a8d;
  --wood-dark:#8a5a2b;
  --wood-light:#c08a52;
  --page-bg:#f7f7f7;
  --ink:#555;
  --ink-soft:#777;
  --navy:#1d3d57;
  --red:#d9545f;
  --red-btn:#a83c45;
  --green:#7dc85e;
  --green-btn:#529a3c;
  --blue:#48a4d4;
  --blue-btn:#2c77a6;
  --gold:#b8862b;
  --black:#111;
  --white:#fff;
}
*{margin:0;padding:0;box-sizing:border-box}
html,body{width:1200px;height:1091px;overflow:hidden}
body{background:var(--page-bg);font-family:"Arimo",Arial,sans-serif;color:var(--ink);position:relative}
.hero{position:absolute;left:0;top:0;width:1200px;height:518px;
  background:radial-gradient(ellipse at 70% 40%,var(--hero-light) 0%,var(--hero-mid) 45%,var(--hero-dark) 100%)}
.shelf{position:absolute;left:0;top:518px;width:1200px;height:60px;
  border-top:4px solid #f1e7dc;
  background:linear-gradient(180deg,var(--wood-light),var(--wood-dark) 60%,#6d4520)}
.brand{position:absolute;left:111px;top:0;width:102px;height:148px;background:linear-gradient(180deg,#2a2a2a,var(--black));
  border:1px solid #444;display:flex;align-items:center;justify-content:center;color:var(--white);
  font-size:17px;font-weight:700;letter-spacing:.5px}
.nav{position:absolute;top:23px;left:660px;display:flex;list-style:none}
.nav a{display:block;height:31px;line-height:31px;color:var(--black);text-decoration:none;font-size:15px;text-transform:uppercase}
.nav .home a{background:var(--black);color:var(--white);border-radius:4px;width:91px;text-align:center}
.nav li:nth-child(2){margin-left:21px}
.nav li:nth-child(3){margin-left:52px}
.nav li:nth-child(4){margin-left:52px}
.hero-title{position:absolute;left:139px;top:190px;color:var(--white);font-size:39px;font-weight:400;letter-spacing:-.3px}
.hero-text{position:absolute;left:139px;top:246px;width:460px;color:var(--white);font-size:14px;line-height:20px}
.step-art{position:absolute;top:345px;width:76px;height:76px;border-radius:6px}
.step-camera{left:164px;background:linear-gradient(135deg,#4e86c4,#1f2a3a)}
.step-photos{left:313px;background:linear-gradient(135deg,#f6f1e8,#e3a14a)}
.step-basket{left:456px;background:linear-gradient(135deg,#ffd43b,#e6a10b)}
.step-arrow{position:absolute;top:366px}
.step-num{position:absolute;top:446px;width:43px;height:43px;border-radius:50%;background:radial-gradient(circle at 40% 35%,#444,#000);
  color:var(--white);font-weight:700;font-size:20px;text-align:center;line-height:43px;box-shadow:0 2px 4px rgba(0,0,0,.4)}
.frame{position:absolute;left:704px;top:93px;width:381px;height:384px;
  background:linear-gradient(135deg,#e8c266,var(--gold) 40%,#6d4a12 100%);
  border:5px solid #2a1a08;padding:24px;box-shadow:0 6px 14px rgba(0,0,0,.4)}
.frame-photo{width:100%;height:100%;border:6px solid #1c1208;
  background:linear-gradient(160deg,#e9e4de,#c9a28a 45%,#8d6a58 80%,#e8dcd3)}
.flourish{position:absolute;top:390px;width:95px;height:60px;border-radius:30px;background:rgba(255,255,255,.18)}
.flourish-left{left:622px}
.flourish-right{left:1070px}
.feature{position:absolute;top:595px;width:358px;height:188px;color:var(--white);padding:0 22px}
.feature-upload{left:55px;background:var(--red)}
.feature-discover{left:422px;background:var(--green)}
.feature-order{left:788px;background:var(--blue)}
.feature h2{font-family:"PT Sans",sans-serif;font-size:28px;font-weight:700;margin-top:12px;height:36px;padding-left:6px}
.feature hr{border:0;border-top:2px dotted rgba(255,255,255,.75);margin:6px 0 9px}
.feature p{font-size:13.5px;line-height:19px}
.more{position:absolute;left:22px;top:137px;width:127px;height:36px;border-radius:3px;color:var(--white);
  font-size:13px;line-height:36px;padding-left:14px;text-transform:uppercase}
.feature-upload .more{background:var(--red-btn)}
.feature-discover .more{background:var(--green-btn)}
.feature-order .more{background:var(--blue-btn)}
.more svg{position:absolute;right:14px;top:11px}
.welcome{position:absolute;left:63px;top:812px;width:715px}
.welcome h1,.testimonials h2{font-family:"PT Sans",sans-serif;font-weight:400;color:var(--navy)}
.welcome h1{font-size:27px;margin-bottom:10px}
.welcome p{font-size:12.5px;line-height:21.8px;color:var(--ink-soft);text-align:justify}
.testimonials{position:absolute;left:828px;top:810px;width:300px}
.testimonials h2{font-size:23px;margin-bottom:12px}
.quote{position:relative;font-size:13px;line-height:21px;color:var(--ink-soft);padding-left:5px}
.quote-mark{position:absolute;left:4px;top:-6px;font-family:"PT Serif",serif;font-size:80px;line-height:70px;color:#e2e2e2}
.quote p{position:relative}
.author{font-family:"PT Serif",serif;font-style:italic;font-size:20px;color:var(--navy);text-align:right;margin-top:10px;padding-right:8px}
.footer{position:absolute;left:0;top:1048px;width:1200px;height:43px;border-top:1px solid #dcdcdc;background:#f1f1f1}
.footer p{position:absolute;left:63px;top:16px;font-size:12px;color:var(--ink-soft)}
.social{position:absolute;left:1003px;top:9px;display:flex;gap:13px}
.social span{width:27px;height:27px;border-radius:50%}
.social .s1{background:#2c5aa0}.social .s2{background:#2fa3d6}.social .s3{background:#f08a1c}.social .s4{background:#c9302c}
</style>
</head>
<body>
<header class="hero">
  <div class="brand">Snaps4Wall</div>
  <ul class="nav">
    <li class="home"><a href="#">Home</a></li>
    <li><a href="#">Upload Photo</a></li>
    <li><a href="#">Pricing</a></li>
    <li><a href="#">Contact Us</a></li>
  </ul>
  <h1 class="hero-title">Lorem ipsum dolor sit amet</h1>
  <p class="hero-text">Lorem ipsum dolor sit amet, consectetuer adipiscing elit. Aenean commodo ligula eget dolor. Aenean massa. Cum sociis. Lorem ipsum dolor sit amet, consectetuer adipiscing elit. Aenean commodo ligula</p>

  <div class="step-art step-camera" role="img" aria-label="Camera with photo icon"></div>
  <svg class="step-arrow" style="left:262px" width="32" height="28" viewBox="0 0 32 28"><path d="M0 9h16V1l15 13-15 13v-8H0z" fill="#111"/></svg>
  <div class="step-art step-photos" role="img" aria-label="Stack of photos icon"></div>
  <svg class="step-arrow" style="left:408px" width="32" height="28" viewBox="0 0 32 28"><path d="M0 9h16V1l15 13-15 13v-8H0z" fill="#111"/></svg>
  <div class="step-art step-basket" role="img" aria-label="Shopping basket icon"></div>
  <div class="step-num" style="left:189px">1</div>
  <div class="step-num" style="left:331px">2</div>
  <div class="step-num" style="left:470px">3</div>

  <div class="flourish flourish-left" role="img" aria-label="White floral ornament"></div>
  <div class="flourish flourish-right" role="img" aria-label="White floral ornament"></div>
  <div class="frame">
    <div class="frame-photo" role="img" aria-label="Family portrait photograph in a gold frame"></div>
  </div>
</header>
<div class="shelf"></div>

<section class="feature feature-upload">
  <h2>Upload</h2><hr>
  <p>Lorem ipsum dolor sit amet, consectetuer adipiscing elit. Aenean commodo ligula eget dolor. Aenean massa. Cum sociis</p>
  <a class="more">Read more<svg width="10" height="14" viewBox="0 0 10 14"><path d="M2 1l6 6-6 6" stroke="#fff" stroke-width="3" fill="none"/></svg></a>
</section>
<section class="feature feature-discover">
  <h2>Discover</h2><hr>
  <p>Lorem ipsum dolor sit amet, consectetuer adipiscing elit. Aenean commodo ligula eget dolor. Aenean massa. Cum sociis</p>
  <a class="more">Read more<svg width="10" height="14" viewBox="0 0 10 14"><path d="M2 1l6 6-6 6" stroke="#fff" stroke-width="3" fill="none"/></svg></a>
</section>
<section class="feature feature-order">
  <h2>Order</h2><hr>
  <p>Lorem ipsum dolor sit amet, consectetuer adipiscing elit. Aenean commodo ligula eget dolor. Aenean massa. Cum sociis</p>
  <a class="more">Read more<svg width="10" height="14" viewBox="0 0 10 14"><path d="M2 1l6 6-6 6" stroke="#fff" stroke-width="3" fill="none"/></svg></a>
</section>

<section class="welcome">
  <h1>Welcome to Snaps 4 Wall</h1>
  <p>Lorem ipsum dolor sit amet, consectetuer adipiscing elit. Aenean commodo ligula eget dolor. Aenean massa. Cum sociis natoque penatibus et magnis dis parturient montes, nascetur ridiculus mus. Donec quam felis, ultricies nec, pellentesque eu, pretium quis, sem. Nulla consequat massa quis enim. Donec pede justo, fringilla vel, aliquet nec, vulputateLorem ipsum doloLorem ipsum dolor sit amet, consectetuer adipiscing elit. Aenean commodo ligula eget dolor. Aenean massa. Cum sociis natoque penatibus et magnis dis parturient montes, nascetur ridiculus mus. Donec quam felis, ultricies nec, pellentesque eu, pretium quis, sem. Nulla consequat massa quis enim. Donec pede justo, fringilla vel, aliquet nec, vulputateLorem ipsum dolor sit amet, consectetuer adipiscing elit. Aenean commodo ligula eget dolor.</p>
</section>

<aside class="testimonials">
  <h2>Testimonials</h2>
  <div class="quote">
    <span class="quote-mark">&ldquo;</span>
    <p>Lorem ipsum dolor sit amet, consectetuer adipiscing elit. Aenean commodo ligula eget dolor. Aenean massa. Cum sociis</p>
  </div>
  <p class="author">- Mark Dalton</p>
</aside>

<footer class="footer">
  <p>Copyright &copy; 2011 &nbsp;Snaps4wall.com . All Rights Reserved. &nbsp;Terms &amp; Conditions &nbsp; | &nbsp; Privacy Policy</p>
  <div class="social"><span class="s1"></span><span class="s2"></span><span class="s3"></span><span class="s4"></span></div>
</footer>
</body>
</html>
```